Webdesign für IT Service Firma
Zielgruppe
Wir sind eine IT-Service Firma und bieten individuelle IT-Lösungen. Unsere Kunden sind KMU, also Firmen mit einer Grösse von 2-250 Mitarbeitern im Grossraum Basel, die in Ihrem Bereich Spezialisten sind und spezielle Anforderungen an Ihre IT besitzen.
Unsere USP sind fixe Ansprechpartner, gute Erreichbarkeit, schneller und individueller Service
Aufgabenstellung
Schriftart Myriad Pro
Grün: #7FA51D
Blau: #4D9BC2
Grau: #999999
Untertitel: Wir sind da.

```html
<!DOCTYPE html>
<html lang="de">
<head>
<meta charset="utf-8">
<title>NORVIKA – IT-Service</title>
<link rel="stylesheet" href="https://fonts.googleapis.com/css2?family=Roboto:wght@300;400;500;700&display=swap">
<style>
  :root {
    --green: #7FA51D;
    --blue: #4D9BC2;
    --grey: #999999;
    --text: #333333;
    --stage: #e9ebed;
    --page: #f2f2f2;
    --card: #ffffff;
  }
  * { box-sizing: border-box; margin: 0; padding: 0; }
  html, body {
    width: 1200px; height: 800px; overflow: hidden;
    background: var(--stage);
    font-family: "Roboto", sans-serif;
    color: var(--text);
  }
  .stage {
    width: 1200px; height: 800px;
    display: flex; justify-content: center; align-items: center;
  }
  .site {
    width: 440px; height: 760px; overflow: hidden;
    background: var(--page);
    border-radius: 6px;
    box-shadow: 0 8px 30px rgba(0,0,0,.12);
    display: flex; flex-direction: column;
  }
  .site-header {
    height: 84px; flex: none;
    background: #fafafa;
    display: flex; align-items: center; justify-content: center;
    position: relative;
  }
  .brand {
    font-size: 34px; font-weight: 400; letter-spacing: 3px;
    color: var(--blue);
  }
  .menu-toggle {
    position: absolute; right: 22px; top: 50%; transform: translateY(-50%);
    width: 34px; height: 30px; border-radius: 3px;
    background: var(--blue);
    display: flex; align-items: center; justify-content: center;
  }
  .hero {
    position: relative; height: 220px; flex: none;
    background: linear-gradient(180deg, #5e9fd8 0%, #a9cbe8 32%, #6f9a4e 55%, #3f7a4a 70%, #3fb3b8 100%);
    display: flex; flex-direction: column; align-items: center; justify-content: center;
    text-align: center; color: #fff; padding: 0 20px;
  }
  .hero-title {
    font-size: 25px; font-weight: 700; letter-spacing: .3px;
    text-shadow: 0 1px 4px rgba(0,0,0,.45);
  }
  .hero-sub {
    margin-top: 6px; font-size: 10px; font-weight: 500; text-transform: uppercase;
    text-shadow: 0 1px 3px rgba(0,0,0,.5);
  }
  .hero-button {
    margin-top: 16px; padding: 7px 20px; border-radius: 16px;
    background: var(--blue); color: #fff; font-size: 11px; letter-spacing: .5px;
  }
  .services { padding: 16px 16px 0; display: flex; flex-direction: column; gap: 14px; flex: none; }
  .service {
    background: var(--card); padding: 16px 18px 18px;
    box-shadow: 0 2px 6px rgba(0,0,0,.08);
  }
  .service-head { display: flex; align-items: center; gap: 12px; margin-bottom: 10px; }
  .service-title { font-size: 17px; font-weight: 500; color: var(--green); text-transform: uppercase; }
  .service p { font-size: 9.5px; line-height: 1.5; margin-bottom: 5px; }
  .service--highlight { background: var(--green); color: #fff; }
  .service--highlight .service-title { color: #fff; }
  .service-button {
    display: inline-block; margin-top: 6px; padding: 6px 12px;
    background: rgba(255,255,255,.18); border: 1px solid rgba(255,255,255,.35);
    color: #fff; font-size: 9.5px; text-transform: uppercase;
  }
  .footer-visual {
    margin-top: 14px; flex: 1;
    background: linear-gradient(180deg, #cfcfcf, #8a8a8a);
  }
</style>
</head>
<body>
<div class="stage">
  <main class="site">
    <header class="site-header">
      <span class="brand">NORVIKA</span>
      <span class="menu-toggle" aria-label="Menü">
        <svg width="18" height="14" viewBox="0 0 18 14"><g stroke="#fff" stroke-width="2"><line x1="0" y1="2" x2="18" y2="2"/><line x1="0" y1="7" x2="18" y2="7"/><line x1="0" y1="12" x2="18" y2="12"/></g></svg>
      </span>
    </header>

    <section class="hero" role="img" aria-label="Stadtansicht mit Münster und Fluss unter blauem Himmel">
      <h1 class="hero-title">WIR KÜMMERN UNS UM IHRE IT</h1>
      <p class="hero-sub">Damit Sie sich auf Ihr Kerngeschäft konzentrieren können.</p>
      <span class="hero-button">WEITERLESEN</span>
    </section>

    <section class="services">
      <article class="service">
        <div class="service-head">
          <svg width="40" height="34" viewBox="0 0 40 34" fill="none" stroke="#7FA51D" stroke-width="1.6">
            <circle cx="16" cy="11" r="6"/>
            <path d="M9 11a7 7 0 0 1 14 0"/>
            <rect x="6" y="22" width="20" height="11" rx="2"/>
            <rect x="28" y="2" width="10" height="7" rx="1"/>
            <path d="M30 9l-1 3 3-3"/>
          </svg>
          <h2 class="service-title">Support</h2>
        </div>
        <p>Sie benötigen eine stabile IT, damit Sie sich voll auf Ihr Kerngeschäft konzentrieren können?</p>
        <p>Sie brauchen einen verlässlichen IT-Dienstleister, der Sie auch in Notfällen nicht im Stich lässt?</p>
        <p>Vertrauen Sie uns, wir kümmern uns um Sie!</p>
      </article>

      <article class="service service--highlight">
        <div class="service-head">
          <svg width="34" height="36" viewBox="0 0 34 36" fill="none" stroke="#fff" stroke-width="1.6">
            <path d="M17 2l13 5v10c0 9-6 15-13 17C10 32 4 26 4 17V7z"/>
            <path d="M17 6l9 3.5v7.5c0 6-4 10.5-9 12-5-1.5-9-6-9-12V9.5z"/>
            <path d="M12 18l4 4 7-8"/>
          </svg>
          <h2 class="service-title">Sicherheit</h2>
        </div>
        <p>Die Daten Ihrer Unternehmung sind die Basis und das Kapital Ihres Geschäfts.</p>
        <p>Ein Verlust oder eine Weitergabe an Dritte bedeutet erhebliche Verluste oder kann gar zur Beendigung Ihres Unternehmens führen.</p>
        <p>Vertrauen Sie uns, wir kümmern uns um Sie!</p>
        <span class="service-button">Kontaktieren Sie uns jetzt</span>
      </article>

      <article class="service">
        <div class="service-head">
          <svg width="44" height="34" viewBox="0 0 44 34" fill="none" stroke="#7FA51D" stroke-width="1.6">
            <circle cx="10" cy="18" r="4"/>
            <path d="M3 32a7 7 0 0 1 14 0"/>
            <circle cx="28" cy="18" r="4"/>
            <path d="M21 32a7 7 0 0 1 14 0"/>
            <rect x="4" y="2" width="14" height="9" rx="1"/>
            <rect x="24" y="2" width="16" height="9" rx="1"/>
          </svg>
          <h2 class="service-title">Beratung</h2>
        </div>
        <p>Ihre IT-Prozesse und Systeme verlangsamen Ihren Arbeitsfluss, anstatt Sie produktiv zu unterstützen?</p>
        <p>Gerne analysieren wir Ihre Infrastruktur und Systeme und helfen Ihnen dabei, Effizienz zu steigern.</p>
        <p>Vertrauen Sie uns, wir kümmern uns um Sie!</p>
      </article>
    </section>

    <div class="footer-visual" role="img" aria-label="Foto eines hellen Büroraums"></div>
  </main>
</div>
</body>
</html>
```